Harvest Bridge Christian Ministry needs a Conference Ad

We are a Christian nonprofit focused on eliminating systemic poverty and helping believers function as ministers in their workplaces. The 2025 Lantern Path Global Conference coming up in October, and we need an ad for social media (facebook, instagram, and X) and our website in order to get people excited to attend! We are looking for a modern and sleek design that incorporates our logo (attached file). You can either put just the butterfly and then write our company name separately somewhere in the design or use it as is (we used Gotham font for the logo). We want to emphasize the joy of in-person connection at the conference, so you could possibly include stock photos of young people gathering together. You could also include the attached photo of our founders in the design and say “with Mel and Dora Quintavan". Also, include the conference dates, which are October 9-12, 2025, and say “come in person or join online”. Lastly, please include the tagline “from the Pellmore Awakening to Worldwide Transformation”. NOTE: I’m attaching AN EXAMPLE I’ve created of how the design could look, which you can feel free to use for inspiration.
Young people on Instagram and facebook
- Gotham

```html
<!DOCTYPE html>
<html lang="en">
<head>
<meta charset="utf-8">
<title>Harvest Bridge – Global Conference Ad</title>
<link href="https://fonts.googleapis.com/css2?family=Montserrat:wght@300;400;700;800&family=Yellowtail&display=swap" rel="stylesheet">
<style>
  :root {
    --stage: #d6d6d6;
    --blue-top: #2340a6;
    --blue-mid: #1a3288;
    --navy: #0b1a45;
    --white: #ffffff;
    --yellow: #f9d31c;
    --gold: #e9c21a;
    --pill-ink: #1d3a9e;
    --photo-warm: #6a5a52;
    --photo-dark: #15161c;
  }
  * { margin: 0; padding: 0; box-sizing: border-box; }
  html, body {
    width: 1200px; height: 796px; overflow: hidden;
    background: var(--stage);
    font-family: "Montserrat", Arial, sans-serif;
  }
  .ad {
    position: absolute; left: 220px; top: 18px;
    width: 760px; height: 760px; overflow: hidden;
    background: linear-gradient(180deg, var(--blue-top) 0%, var(--blue-mid) 45%, var(--navy) 100%);
    color: var(--white);
  }
  .brand {
    position: absolute; left: 600px; top: 52px; width: 126px;
    text-align: right; font-weight: 700; font-size: 17px; line-height: 1.05;
    letter-spacing: 0.5px; color: var(--white);
  }
  .brand-dot {
    display: block; width: 46px; height: 46px; border-radius: 50%;
    background: var(--white); margin: 0 0 10px auto;
  }
  .tagline {
    position: absolute; left: 46px; top: 88px;
    text-transform: uppercase; line-height: 53px; letter-spacing: 1px;
  }
  .tagline .light { font-weight: 300; font-size: 52px; }
  .tagline .bold { font-weight: 800; font-size: 47px; }
  .tagline .line-one { font-weight: 300; font-size: 52px; }
  .event-pill {
    position: absolute; left: 46px; top: 329px; width: 371px; height: 53px;
    border-radius: 27px; background: var(--yellow);
    display: flex; align-items: center; justify-content: center;
    font-family: "Yellowtail", cursive; font-size: 44px; color: var(--pill-ink);
    padding-top: 4px;
  }
  .founders-photo {
    position: absolute; left: 0; top: 405px; width: 499px; height: 355px;
    background: radial-gradient(ellipse at 45% 40%, var(--photo-warm) 0%, var(--photo-dark) 70%);
    border-radius: 200px 220px 0 0;
    opacity: 0.9;
  }
  .dates {
    position: absolute; right: 34px; top: 358px; text-align: center; width: 160px;
  }
  .dates .days { font-weight: 700; font-size: 68px; line-height: 66px; }
  .dates .month { font-weight: 400; font-size: 29px; line-height: 28px; color: var(--yellow); letter-spacing: 1px; }
  .dates .year { font-weight: 800; font-size: 52px; line-height: 46px; color: var(--gold); letter-spacing: 3px; }
  .attend {
    position: absolute; right: 34px; top: 514px; text-align: right;
    font-weight: 300; font-size: 28px; line-height: 34px;
  }
  .attend .online { color: var(--yellow); }
  .hosts {
    position: absolute; left: 545px; top: 676px; width: 230px; height: 58px;
    border: 2px solid var(--yellow); border-right: none; border-radius: 30px 0 0 30px;
    text-align: right; padding: 6px 49px 0 0;
    font-weight: 300; font-size: 22px; line-height: 23px;
  }
</style>
</head>
<body>
  <main class="ad">
    <div class="brand"><span class="brand-dot"></span>HARVEST<br>BRIDGE</div>

    <h1 class="tagline">
      <span class="line-one">From the</span><br>
      <span class="bold">Pellmore Awakening</span><br>
      <span class="light">To</span> <span class="bold">Worldwide</span><br>
      <span class="bold">Transformation</span>
    </h1>

    <div class="event-pill">Global Conference</div>

    <div class="founders-photo" role="img" aria-label="Photo of founders Mel and Dora Quintavan smiling together"></div>

    <div class="dates">
      <div class="days">9-12</div>
      <div class="month">OCTOBER</div>
      <div class="year">2025</div>
    </div>

    <p class="attend">Come in-person<br>or <span class="online">Join Online</span></p>

    <p class="hosts">with Mel &amp;<br>Dora Quintavan</p>
  </main>
</body>
</html>
```